Professional looking website for solo practitioner law practice

I have recently started up my new law practice. Currently there is just myself practicing here. I would like to have a website that provides my contact information, a map, and the different areas of law that I practice in, being Family Litigation, Wills & Estates, Corporate/Commerical, and Real Estate. I recently had a logo designed so I would like the colours of my website to be congruent with that and include the logo.
I am located in Edmonton, Alberta.

Reason: I will be away for the next few days.

Target Market(s)

individuals and families with an income of $50K+, mostly those looking for family lawyer re divorce, child support, custody and parenting, spousal support.

Industry/Entity Type

Lawyer

Number of Pages Required

4 page

Font styles to use
Serif

Colors
0355a3

Requirements
Must have
• Contact information, ability to email me, background picture(s) that are professional and fit with the legal services theme/service provided but are not single individual lawyers, gavels, or court houses. Need to have click to change the text to include information on Family Litigation, Wills & Estates, Corporate/Commercial, and Real Estate
Nice to have
• contact box
Should not have
• blog, sans serif text, testimonials, news

```html
<!DOCTYPE html>
<html lang="en">
<head>
<meta charset="utf-8">
<title>Marlow Hart Law Office</title>
<link rel="stylesheet" href="https://fonts.googleapis.com/css2?family=Cinzel:wght@400;600;700&family=Raleway:wght@400;600;700&display=swap">
<style>
:root{
  --blue:#0355a3;
  --navy:#1b2f80;
  --deep:#17328a;
  --grey:#6d6d6d;
  --text:#555;
  --light:#f2f2f2;
  --gold:#f5d88a;
  --amber:#c98a2a;
  --white:#fff;
}
*{box-sizing:border-box;margin:0;padding:0}
html,body{width:755px;height:1200px;overflow:hidden}
body{position:relative;font-family:"Raleway",sans-serif;color:var(--text);background:var(--white)}

/* header */
.site-header{position:absolute;left:0;top:0;width:755px;height:67px;background:var(--white)}
.brand{position:absolute;left:42px;top:10px;display:flex;align-items:center;gap:10px;color:var(--navy);font-family:"Cinzel",serif;font-weight:600}
.brand-mark{width:46px;height:46px;border:3px solid var(--navy)}
.brand-name{font-size:24px;line-height:25px}
.brand-sub{font-size:11px;letter-spacing:4.5px;line-height:14px;text-align:center}
.header-contact{position:absolute;left:574px;font-size:10.5px;font-weight:700;color:#222;display:flex;align-items:center;gap:6px}
.icon-box{width:17px;height:17px;border:1.5px solid var(--blue);display:flex;align-items:center;justify-content:center}

/* nav */
.main-nav{position:absolute;left:0;top:67px;width:755px;height:28px;background:var(--blue)}
.main-nav a{position:absolute;top:0;height:28px;line-height:28px;text-align:center;color:var(--white);font-family:"Cinzel",serif;font-weight:600;font-size:11.5px;text-decoration:none;border-right:1px solid rgba(255,255,255,.35)}
.main-nav a.active{background:var(--grey)}

/* hero */
.hero{position:absolute;left:0;top:95px;width:755px;height:267px;background:var(--amber)}
.hero-mark{position:absolute;left:654px;top:35px;width:58px;height:58px;border:3px solid rgba(110,70,20,.5)}
.hero-title{position:absolute;right:43px;top:108px;text-align:right;font-family:"Cinzel",serif;font-weight:700;font-size:21px;line-height:26px;color:var(--gold)}
.hero-btn{position:absolute;left:475px;top:171px;width:237px;height:32px;background:var(--grey);border:1px solid var(--white);color:var(--white);font-family:"Cinzel",serif;font-weight:600;font-size:15px;line-height:30px;text-align:center}
.hero-dots{position:absolute;left:669px;top:222px;display:flex;gap:4px}
.hero-dots span{width:12px;height:2px;background:var(--white)}
.hero-dots span:first-child{background:#6aa0e0}

/* welcome */
.welcome{position:absolute;left:0;top:362px;width:755px;height:278px;background:var(--light)}
.welcome-mark{position:absolute;left:43px;top:32px;width:30px;height:30px;border:2.5px solid var(--navy)}
.welcome-title{position:absolute;left:86px;top:38px;font-family:"Cinzel",serif;font-weight:600;font-size:18.5px;color:var(--navy);white-space:nowrap}
.welcome-title span,.form-title span,.section-title span{color:var(--grey)}
.welcome-lead{position:absolute;left:43px;top:76px;width:430px;font-size:10.5px;font-weight:700;line-height:15px;color:var(--blue)}
.welcome-body{position:absolute;left:43px;top:114px;width:430px;font-size:8.6px;line-height:17px;color:#444}
.pill-btn{position:absolute;display:flex;align-items:center;background:var(--blue);color:var(--white);font-weight:700;text-transform:uppercase}
.pill-btn .arrow{position:absolute;border-radius:50%;background:var(--grey);border:2px solid var(--white);display:flex;align-items:center;justify-content:center}
.evaluation{position:absolute;left:502px;top:36px;width:208px;height:212px;background:var(--white);border:2px solid var(--navy)}
.form-title{position:absolute;left:11px;top:18px;font-family:"Cinzel",serif;font-weight:600;font-size:16px;color:var(--navy);white-space:nowrap}
.field{position:absolute;left:11px;width:185px;border:1px solid #ccc;background:var(--white);font-size:8.5px;color:#555;padding:7px 7px}

/* practice */
.section-title{position:absolute;left:0;top:664px;width:755px;text-align:center;font-family:"Cinzel",serif;font-weight:600;font-size:18.5px;color:var(--navy)}
.divider{position:absolute;top:704px;height:1px;background:#ddd}
.divider-mark{position:absolute;left:369px;top:695px;width:19px;height:19px;border:1.5px solid #bbb;background:var(--white)}
.area{position:absolute;top:748px;width:150px;text-align:center}
.area-icon{width:67px;height:67px;margin:0 auto;border:3px solid var(--blue);display:flex;align-items:center;justify-content:center}
.area h3{margin-top:14px;font-size:12.5px;font-weight:600;color:var(--text)}
.area p{margin:6px auto 0;width:126px;font-size:8px;line-height:10.5px;color:#444}
.area .more{margin-top:5px;font-size:8px;color:#333}

/* cta */
.cta{position:absolute;left:0;top:924px;width:755px;height:82px;background:#6e6e6e}
.cta-text{position:absolute;right:261px;top:16px;text-align:right;font-family:"Cinzel",serif;font-weight:600;font-size:19.5px;line-height:23px;color:var(--white)}
.cta-btn{position:absolute;left:557px;top:25px;width:141px;height:30px;background:var(--navy);border:1px solid var(--white);color:var(--white);font-weight:600;font-size:15px;line-height:28px;text-align:center}

/* footer */
.site-footer{position:absolute;left:0;top:1006px;width:755px;height:166px;background:var(--blue);color:var(--white)}
.footer-title{position:absolute;top:24px;font-family:"Cinzel",serif;font-weight:600;font-size:12px;letter-spacing:.5px}
.footer-rule{position:absolute;height:1px;background:rgba(255,255,255,.15)}
.footer-sep{position:absolute;top:20px;width:1px;height:130px;background:rgba(255,255,255,.15)}
.quick-links{position:absolute;left:42px;top:52px;list-style:none}
.quick-links li{font-size:7.5px;font-weight:700;text-transform:uppercase;line-height:17.6px}
.quick-links li::before{content:"•";margin-right:6px}
.map{position:absolute;left:190px;top:52px;width:163px;height:79px;background:#e3e3dc;border:2px solid var(--white)}
.detail{position:absolute;left:370px;display:flex;gap:6px;font-size:7.5px;line-height:12px}
.detail b{font-size:6.5px;text-transform:uppercase}
.footer-brand{position:absolute;left:574px;top:60px;display:flex;align-items:center;gap:7px;font-family:"Cinzel",serif;font-weight:600}
.footer-brand .brand-mark{width:27px;height:27px;border:2px solid var(--white)}
.footer-brand .brand-name{font-size:14px;line-height:15px}
.footer-brand .brand-sub{font-size:6.5px;letter-spacing:3px;line-height:9px}
.social{position:absolute;top:109px;width:21px;height:21px;border-radius:50%;background:var(--deep);border:1.5px solid var(--white)}
.social.red{background:#d9342b}
.social.sky{background:#2b9fdc}
.copyright{position:absolute;left:0;top:1172px;width:755px;height:28px;background:var(--deep);color:#d5ddf0;font-size:7.5px;text-align:center;line-height:28px}
</style>
</head>
<body>

<header class="site-header">
  <div class="brand">
    <div class="brand-mark"></div>
    <div><div class="brand-name">Marlow Hart</div><div class="brand-sub">Law Office</div></div>
  </div>
  <div class="header-contact" style="top:15px">
    <span class="icon-box"><svg width="10" height="8" viewBox="0 0 10 8"><rect x="0.5" y="0.5" width="9" height="7" fill="none" stroke="#0355a3"/><path d="M0.5 0.5 5 4.5 9.5 0.5" fill="none" stroke="#0355a3"/></svg></span>555-014-2290
  </div>
  <div class="header-contact" style="top:37px">
    <span class="icon-box"><svg width="10" height="10" viewBox="0 0 10 10"><path d="M2 1l2 2-1 1.5c.7 1.3 1.5 2.1 2.5 2.5L7 6l2 2-1.5 1.5C4 9 1 6 0.5 2.5z" fill="#0355a3"/></svg></span>info@marlowhart.com
  </div>
</header>

<nav class="main-nav">
  <a class="active" style="left:43px;width:87px">Home</a>
  <a style="left:130px;width:121px">About</a>
  <a style="left:251px;width:174px">Practice Areas</a>
  <a style="left:425px;width:167px">Testimonials</a>
  <a style="left:592px;width:118px;border-right:0">Contact</a>
</nav>

<section class="hero" role="img" aria-label="Photo of a family silhouetted against a golden sunset">
  <div class="hero-mark"></div>
  <h1 class="hero-title">Realize Your Constitutional<br>Right For Qualified Legal Help</h1>
  <div class="hero-btn">Get A Free Consultation</div>
  <div class="hero-dots"><span></span><span></span><span></span></div>
</section>

<section class="welcome">
  <div class="welcome-mark"></div>
  <h2 class="welcome-title">Welcome To Marlow Hart <span>Law Office</span></h2>
  <p class="welcome-lead">Lorem ipsum dolor sit amet, consectetuer adipiscing elit, sed diam nonummy nibh euismod tincidunt ut laoreet dolore magna aliquam erat volutpat.</p>
  <p class="welcome-body">Lorem ipsum dolor sit amet, consectetuer adipiscing elit, sed diam nonummy nibh euismod tincidunt ut laoreet dolore magna aliquam erat volutpat. Ut wisi enim ad minim veniam, quis nostrud exerci tation ullamcorper suscipit lobortis nisl ut aliquip ex ea commodo consequat. Duis autem vel eum iriure dolor in hendrerit in vulputate velit esse molestie consequat, vel illum dolore eu feugiat nulla facilisis at vero eros et accumsan et iusto odio dignissim qui blandit praesent luptatum zzril delenit augue duis dolore te feugait nulla facilisis.</p>
  <div class="pill-btn" style="left:43px;top:223px;width:72px;height:19px;font-size:7.5px;padding-left:5px">Read More
    <span class="arrow" style="left:57px;top:-1px;width:21px;height:21px"><svg width="6" height="8" viewBox="0 0 6 8"><path d="M1 1l3 3-3 3" fill="none" stroke="#fff" stroke-width="1.3"/></svg></span>
  </div>

  <form class="evaluation">
    <h2 class="form-title">Free Case <span>Evaluation</span></h2>
    <div class="field" style="top:52px;height:25px">Name</div>
    <div class="field" style="top:83px;height:25px">Email</div>
    <div class="field" style="top:114px;height:47px">Message</div>
    <div class="pill-btn" style="left:11px;top:172px;width:60px;height:22px;font-size:9.5px;padding-left:8px">Submit
      <span class="arrow" style="left:52px;top:-2px;width:26px;height:26px"><svg width="6" height="9" viewBox="0 0 6 9"><path d="M1 1l3.5 3.5L1 8" fill="none" stroke="#fff" stroke-width="1.3"/></svg></span>
    </div>
  </form>
</section>

<h2 class="section-title">Our <span>Practice Areas</span></h2>
<div class="divider" style="left:272px;width:90px"></div>
<div class="divider" style="left:394px;width:90px"></div>
<div class="divider-mark"></div>

<div class="area" style="left:51px">
  <div class="area-icon"><svg width="40" height="30" viewBox="0 0 40 30"><g fill="#0355a3"><circle cx="9" cy="5" r="3.5"/><rect x="5.5" y="10" width="7" height="12" rx="2"/><rect x="6" y="20" width="2.5" height="9"/><rect x="9.5" y="20" width="2.5" height="9"/><circle cx="31" cy="5" r="3.5"/><path d="M27 10h8l3 12h-14z"/><rect x="28" y="20" width="2.5" height="9"/><rect x="31.5" y="20" width="2.5" height="9"/><circle cx="20" cy="14" r="2.5"/><rect x="17.5" y="18" width="5" height="11" rx="1.5"/></g></svg></div>
  <h3>Family&nbsp; Litigation</h3>
  <p>Lorem ipsum dolor sit amet, consectetuer Lorem ipsum dolor sit amet, consectetuer</p>
  <div class="more">[+]</div>
</div>
<div class="area" style="left:213px">
  <div class="area-icon"><svg width="30" height="30" viewBox="0 0 30 30"><rect x="4" y="4" width="18" height="22" fill="none" stroke="#0355a3" stroke-width="2.2"/><path d="M8 10h10M8 14h10M8 18h6" stroke="#0355a3" stroke-width="2"/><path d="M18 22l8-10 2 2-8 10h-2z" fill="#0355a3"/></svg></div>
  <h3>Wills &amp; Estates</h3>
  <p>Lorem ipsum dolor sit amet, consectetuer Lorem ipsum dolor sit amet, consectetuer</p>
  <div class="more">[+]</div>
</div>
<div class="area" style="left:383px">
  <div class="area-icon"><svg width="34" height="30" viewBox="0 0 34 30"><rect x="2" y="8" width="30" height="19" rx="2" fill="none" stroke="#0355a3" stroke-width="2.2"/><path d="M12 8V4h10v4M2 16h30" fill="none" stroke="#0355a3" stroke-width="2.2"/><rect x="14" y="14" width="6" height="5" fill="#0355a3"/></svg></div>
  <h3>Corporate/Commercial</h3>
  <p>Lorem ipsum dolor sit amet, consectetuer Lorem ipsum dolor sit amet, consectetuer</p>
  <div class="more">[+]</div>
</div>
<div class="area" style="left:555px">
  <div class="area-icon"><svg width="30" height="34" viewBox="0 0 30 34"><rect x="7" y="2" width="16" height="28" fill="#0355a3"/><rect x="3" y="29" width="24" height="3" fill="#0355a3"/><g fill="#fff"><rect x="10" y="6" width="3" height="3"/><rect x="17" y="6" width="3" height="3"/><rect x="10" y="12" width="3" height="3"/><rect x="17" y="12" width="3" height="3"/><rect x="10" y="18" width="3" height="3"/><rect x="17" y="18" width="3" height="3"/></g></svg></div>
  <h3>Real Estate</h3>
  <p>Lorem ipsum dolor sit amet, consectetuer Lorem ipsum dolor sit amet, consectetuer</p>
  <div class="more">[+]</div>
</div>

<section class="cta">
  <p class="cta-text">For Any Legal Problem, We Can Help You<br>Anytime Take An Appointment Now</p>
  <div class="cta-btn">CONTACT US</div>
</section>

<footer class="site-footer">
  <h4 class="footer-title" style="left:42px">Quick Links</h4>
  <div class="footer-rule" style="left:42px;top:46px;width:95px"></div>
  <ul class="quick-links">
    <li>Home</li><li>About Us</li><li>Practice Area</li><li>Testimonials</li><li>Contact Us</li>
  </ul>
  <div class="footer-sep" style="left:157px"></div>
  <h4 class="footer-title" style="left:188px">Contact Details</h4>
  <div class="footer-rule" style="left:188px;top:46px;width:305px"></div>
  <div class="map" role="img" aria-label="Street map showing the office location"></div>
  <div class="detail" style="top:54px">
    <svg width="8" height="11" viewBox="0 0 8 11"><path d="M4 0a4 4 0 0 0-4 4c0 3 4 7 4 7s4-4 4-7a4 4 0 0 0-4-4z" fill="#fff"/><circle cx="4" cy="4" r="1.5" fill="#0355a3"/></svg>
    <div><b>Marlow Hart Law Office</b><br>consectetur adipiscing elit,<br>Sed vitae magna - 12345.</div>
  </div>
  <div class="detail" style="top:100px;font-weight:700">
    <svg width="9" height="9" viewBox="0 0 10 10"><path d="M2 1l2 2-1 1.5c.7 1.3 1.5 2.1 2.5 2.5L7 6l2 2-1.5 1.5C4 9 1 6 0.5 2.5z" fill="#fff"/></svg>555-014-2290
  </div>
  <div class="detail" style="top:123px;font-weight:600">
    <svg width="9" height="7" viewBox="0 0 10 8"><rect x="0.5" y="0.5" width="9" height="7" fill="none" stroke="#fff"/><path d="M0.5 0.5 5 4.5 9.5 0.5" fill="none" stroke="#fff"/></svg>info@marlowhart.com
  </div>
  <div class="footer-sep" style="left:545px"></div>
  <div class="footer-brand">
    <div class="brand-mark"></div>
    <div><div class="brand-name">Marlow Hart</div><div class="brand-sub">Law Office</div></div>
  </div>
  <span class="social" style="left:592px" aria-label="Social link"></span>
  <span class="social" style="left:619px" aria-label="Social link"></span>
  <span class="social sky" style="left:647px" aria-label="Social link"></span>
  <span class="social red" style="left:675px" aria-label="Social link"></span>
</footer>

<div class="copyright">Copyright © 2016 MARLOW HART LAW OFFICE.&nbsp; All Rights Reserved.</div>

</body>
</html>
```